Real Estate Brokerage Informational Handbill

A 4 X 6 handbill to promote a real estate brokerage modeled after the design attached including attached logo and information.
These handbills should provide a high-level overview of what we do at the brokerage and should be attractive and be inviting.
The goal of the handbill is to have motivated clients in the market to buy or sell their home or property call or visit our website

Target Market(s)

Buyers and sellers of real estate in the Rochester NY area ages 24 - 60

Industry/Entity Type

Real Estate

Font styles to use
Sans Serif

Requirements
Must have
• Please include all the information contained on current handbill
• remove the line "we will walk you through the home buying process at no cost to you".
• replace with "come to one of our monthly first-time buyer informational sessions".
• add the phrase "have your reviewed and receive customized Home Purchase Plan"
• Add the slogan "Bright Gate Realty Helping Motivated People Achieve Their Real Estate Goals"
Nice to have
• 2 sided design

```html
<!DOCTYPE html>
<html lang="en">
<head>
<meta charset="utf-8">
<title>Bright Gate Realty – Handbill</title>
<link rel="stylesheet" href="https://fonts.googleapis.com/css2?family=Cinzel:wght@400;600&family=Open+Sans:ital,wght@0,400;0,600;0,700;0,800;1,600&display=swap">
<style>
  :root {
    --stage: #e6e6e2;
    --card: #fbfbfa;
    --photo-light: #f1f1ef;
    --photo-mid: #d9d9d6;
    --photo-warm: #cfc2bb;
    --ink: #2b2b2b;
    --brand-slate: #3a4450;
    --band-pink: #e05a75;
    --band-pink-deep: #d9506c;
    --band-yellow: #f2c12e;
    --white: #ffffff;
  }
  * { box-sizing: border-box; margin: 0; padding: 0; }
  html, body {
    width: 1200px;
    height: 800px;
    overflow: hidden;
    background: var(--stage);
  }
  .handbill {
    position: absolute;
    top: 210px;
    width: 570px;
    height: 380px;
    background: var(--card);
    overflow: hidden;
    box-shadow: 0 2px 8px rgba(0,0,0,0.12);
  }
  .handbill--front { left: 20px; }
  .handbill--back  { left: 610px; font-family: 'Open Sans', sans-serif; color: var(--ink); }

  /* Front */
  .hero-photo {
    position: absolute;
    left: 0; top: 0;
    width: 100%; height: 235px;
    background:
      radial-gradient(ellipse 22% 40% at 25% 48%, var(--photo-warm), transparent 70%),
      radial-gradient(ellipse 30% 45% at 70% 40%, var(--photo-mid), transparent 75%),
      linear-gradient(180deg, var(--photo-light) 0%, var(--photo-light) 70%, var(--card) 100%);
  }
  .slogan {
    position: absolute;
    left: 30px; top: 240px;
    font-family: 'Cinzel', serif;
    font-weight: 400;
    font-size: 23px;
    line-height: 27px;
    color: var(--ink);
  }
  .front-brand {
    position: absolute;
    left: 385px; top: 258px;
    width: 165px;
    text-align: center;
    font-family: 'Cinzel', serif;
    font-weight: 600;
    font-size: 19px;
    line-height: 23px;
    color: var(--brand-slate);
  }
  .band { position: absolute; left: 0; }
  .band--pink   { top: 328px; width: 505px; height: 10px; background: var(--band-pink); }
  .band--yellow { top: 341px; width: 490px; height: 7px;  background: var(--band-yellow); }

  /* Back */
  .specialists {
    position: absolute;
    right: 24px; top: 14px;
    font-size: 22px; font-weight: 600;
    line-height: 28px;
    text-align: right;
  }
  .services-intro {
    position: absolute;
    right: 24px; top: 46px;
    font-size: 19px; font-weight: 600;
    line-height: 26px;
    text-align: right;
  }
  .closing {
    position: relative;
    font-weight: 800;
    text-transform: uppercase;
  }
  .closing-swoosh {
    position: absolute;
    left: 10%; bottom: -8px;
    width: 80%; height: 8px;
  }
  .session-banner {
    position: absolute;
    left: 0; top: 106px;
    width: 530px; height: 26px;
    padding: 0 18px 0 24px;
    background: var(--band-yellow);
    border-radius: 0 13px 13px 0;
    font-size: 13px; font-weight: 700;
    line-height: 26px;
    text-align: right;
    white-space: nowrap;
  }
  .purchase-plan {
    position: absolute;
    right: 24px; top: 140px;
    font-size: 17px; font-weight: 600;
    line-height: 23px;
    text-align: right;
  }
  .purchase-plan strong { font-weight: 800; }
  .consult-panel {
    position: absolute;
    left: 0; top: 205px;
    width: 100%; height: 175px;
    background: var(--band-pink);
  }
  .consult-photo {
    position: absolute;
    inset: 0;
    background:
      radial-gradient(ellipse 30% 55% at 65% 45%, rgba(255,255,255,0.22), transparent 70%),
      linear-gradient(90deg, var(--band-pink) 0%, var(--band-pink-deep) 100%);
  }
  .back-brand {
    position: absolute;
    right: 24px; top: 14px;
    font-size: 18px; font-weight: 700;
    line-height: 22px;
    color: var(--white);
  }
  .counseling {
    position: absolute;
    left: 24px; top: 16px;
    font-size: 15px; font-weight: 600;
    color: var(--white);
  }
  .consult-rule {
    position: absolute;
    left: 0; top: 92px;
    width: 100%; height: 3px;
    background: var(--band-yellow);
  }
  .consult-offer {
    position: absolute;
    left: 24px; top: 99px;
    font-size: 14px; font-style: italic; font-weight: 600;
    color: var(--ink);
  }
  .phone {
    position: absolute;
    left: 24px; top: 118px;
    font-size: 36px; font-weight: 800;
    line-height: 46px;
    color: var(--ink);
    letter-spacing: 0.5px;
  }
</style>
</head>
<body>
  <main class="handbill handbill--front">
    <div class="hero-photo" role="img" aria-label="Photo of a small model house with a red and white facade beside a hand signing a contract, with house keys on the paper"></div>
    <h1 class="slogan">Helping Motivated People<br>Achieve Their<br>Real Estate Goals</h1>
    <p class="front-brand">Bright Gate<br>Realty</p>
    <div class="band band--pink"></div>
    <div class="band band--yellow"></div>
  </main>

  <section class="handbill handbill--back">
    <h2 class="specialists">First Time Home Buyer's Specialists</h2>
    <p class="services-intro">
      Assisting you with all of your real estate<br>
      needs from start to <span class="closing">Closing<svg class="closing-swoosh" viewBox="0 0 100 8" preserveAspectRatio="none"><path d="M2 2 Q50 9 98 2" stroke="#e05a75" stroke-width="3" fill="none"/></svg></span> and beyond
    </p>
    <p class="session-banner">Come to one of our monthly first-time buyer informational sessions</p>
    <p class="purchase-plan">
      Have your credit reviewed and receive personalized<br>
      <strong>Home Purchase Plan</strong>
    </p>
    <div class="consult-panel">
      <div class="consult-photo" role="img" aria-label="Faded photo of a handshake in front of a house, tinted pink"></div>
      <p class="counseling">Buyer &amp; seller counseling</p>
      <p class="back-brand">Bright Gate Realty</p>
      <div class="consult-rule"></div>
      <p class="consult-offer">Call for a free consultation</p>
      <p class="phone">(555) 010-HOME</p>
    </div>
  </section>
</body>
</html>
```